Exciting adult social quiz app needs awesome modern design

A new and exciting app for couples/sexual partners is in the making. It will be available for Orvane and Quillo devices and allow one partner to invite another partner to the game. The partners will answer questions about their sexual desires and needs and then try to guess what the other one answered.

The app needs a high quality design and you can find some general inspiration in a similar social quiz app called "Pear Trail" which can be found in Gadget Depot and Fetch Market. I like some of the basic layouts of this app.

The design should be classy and have a theme that matches the app subject. This is a sexual get-to-know-each-other-app and not a "porn app". I imagine colors might be black and red (not a requirement) and perhaps have some structures, pictures or backgrounds showing a bit of skin. It's important that the game can be accessed by players in the public space (e.g. in a bus, car etc.) without surroundings thinking it's a sex/porn game - but also important that it's exciting in a kind of sexual way. So try to find a fine line.

As the app is for both genders, the design should accommodate this.

Please see app mockups in the attached PDF.

Initially, please show design proposals for screens 13, 16 and 23.
Please notice that screen 16 doesn't have to be exactly those 2 bars - please make some alternative score comparison graphic in your proposal.

Looking forward to seeing your proposal soon!

Target Market(s)

Couples between 18 and 50

Industry/Entity Type

Adult

Requirements
Must have
• Smooth graphics like the app "Pear Trail"
Nice to have
• Several proposals are appreciated. Perhaps you can show your proposals with different colors and object placements so that I can see some different options.

```html
<!DOCTYPE html>
<html lang="en">
<head>
<meta charset="utf-8">
<title>Couples Quiz – Screen Proposals</title>
<link href="https://fonts.googleapis.com/css2?family=Inter:wght@400;500;600&display=swap" rel="stylesheet">
<style>
:root{
  --orange-top:#fdcd86;
  --orange-bottom:#fbb55e;
  --orange-text:#f8b157;
  --body-bg:#e6e6e4;
  --ink:#111111;
  --muted:#555555;
  --faint:#9a9a9a;
  --white:#ffffff;
  --ring-his:#2f7ee3;
  --ring-hers:#c935ea;
  --photo-warm-a:#8a5a3c;
  --photo-warm-b:#3a2a24;
  --photo-dark-a:#5b4a3f;
  --photo-dark-b:#1e1a18;
  --page:#ffffff;
}
*{box-sizing:border-box;margin:0;padding:0}
html,body{width:1200px;height:724px;overflow:hidden;background:var(--page)}
body{font-family:"Inter",Helvetica,Arial,sans-serif;color:var(--ink)}
.stage{position:relative;width:1380px;height:832px;transform:scale(0.86957);transform-origin:0 0}
.screen{position:absolute;top:131px;width:320px;height:569px;background:var(--body-bg);overflow:hidden;box-shadow:0 0 3px rgba(0,0,0,.25)}
.screen--round{left:10px}
.screen--collect{left:343px}
.screen--chat{left:674px}
.screen--sent{left:1032px}

.topbar{position:absolute;left:0;top:0;width:100%;height:65px;background:linear-gradient(var(--orange-top),var(--orange-bottom));z-index:2}
.status{display:flex;justify-content:space-between;align-items:center;height:20px;padding:0 6px;font-size:11px;color:var(--white)}
.status__carrier{display:flex;align-items:center;gap:4px}
.status__battery{display:flex;align-items:center;gap:4px}
.battery{width:22px;height:10px;border:1px solid var(--white);border-radius:2px;padding:1px}
.battery span{display:block;width:100%;height:100%;background:var(--white)}
.title{height:45px;display:flex;align-items:center;justify-content:center;font-size:17px;font-weight:500}

.content{position:absolute;left:0;top:65px;width:100%;height:456px}
.prompt{text-align:center;font-size:16px;line-height:23px;color:var(--muted);margin-top:12px}
.player{position:absolute;left:34px;width:300px;height:144px}
.player--his{top:70px}
.player--hers{top:232px}
.player__ring{position:absolute;left:0;top:0}
.player__name{position:absolute;left:181px;top:38px;font-size:20px}
.player__score{position:absolute;left:168px;top:68px;font-size:32px;font-weight:400}
.btn-continue{position:absolute;left:0;top:393px;width:100%;height:42px;background:linear-gradient(var(--orange-top),var(--orange-bottom));display:flex;align-items:center;justify-content:center;font-size:20px}

.ad{position:absolute;left:0;top:521px;width:100%;height:48px;background:var(--white);padding:0}
.ad__music{position:absolute;inset:0;background:linear-gradient(90deg,#2a7d73,#6b3c6e 30%,#b63e4a 55%,#2c6ca0 75%,#d9a13a)}
.ad__line{position:absolute;left:6px;top:8px;font-size:12px;color:var(--white)}
.ad__chip{position:absolute;left:6px;top:31px;background:#f26b1d;color:var(--white);font-size:5px;font-weight:600;padding:2px 5px}
.ad__brand{position:absolute;right:14px;top:22px;font-size:13px;font-weight:600;color:var(--white)}
.ad__tag{position:absolute;right:3px;bottom:2px;font-size:8px;color:#333}
.ad__slots{position:absolute;inset:0;background:linear-gradient(90deg,#f3e6c6,#f7efd8 40%,#f0dca9);border-bottom:2px solid #d63b8a}
.ad__store{position:absolute;left:4px;top:4px;height:20px;padding:0 6px;background:#111;color:var(--white);font-size:8px;border-radius:3px;display:flex;align-items:center}
.ad__tiles{position:absolute;left:80px;top:3px;display:flex;gap:3px}
.ad__tile{width:52px;height:42px;background:linear-gradient(#fff3d6,#f5d98a);border:1px solid #e2c27a}
.ad__play{position:absolute;right:12px;top:24px;background:#d83579;color:var(--white);font-size:11px;font-weight:600;padding:2px 5px;border-radius:3px}

.dimmed{position:absolute;inset:0;filter:blur(2px)}
.scrim{position:absolute;left:0;top:65px;width:100%;height:456px;background:rgba(0,0,0,.42);z-index:3}
.topbar-scrim{position:absolute;left:0;top:20px;width:100%;height:45px;z-index:3}
.sheet{position:absolute;left:25px;top:155px;width:269px;height:261px;background:#f4f4f4;border-radius:12px;overflow:hidden;z-index:4}
.sheet__title{height:36px;display:flex;align-items:center;justify-content:center;color:var(--orange-text);font-size:17px;font-weight:500;background:var(--white)}
.sheet__list{list-style:none}
.sheet__item{background:var(--white);border-top:1px solid #d8d8d8;text-align:center;font-size:16px;line-height:20px;padding:5px 20px;color:#222}
.sheet__btn{position:absolute;left:0;bottom:0;width:100%;height:43px;background:linear-gradient(var(--orange-top),var(--orange-bottom));display:flex;align-items:center;justify-content:center;font-size:16px;font-weight:600}

.profile{position:absolute;left:0;top:65px;width:100%;height:96px}
.profile__name{position:absolute;left:170px;top:0;width:150px;height:48px;display:flex;align-items:center;justify-content:center;font-size:22px;background:var(--white)}
.profile__nudge{position:absolute;left:160px;top:48px;width:160px;height:44px;background:linear-gradient(var(--orange-top),var(--orange-bottom));display:flex;align-items:center;justify-content:center;gap:14px;font-size:20px}
.chat__label{position:absolute;left:0;top:183px;width:100%;text-align:center;font-size:16px;color:#333}
.msg{position:absolute;display:flex;align-items:center;gap:6px}
.msg--in{left:18px;top:210px}
.msg--out{right:18px;top:278px}
.avatar{width:46px;height:46px;border-radius:50%;border:2px solid var(--white);background:radial-gradient(circle at 50% 40%,var(--photo-warm-a),var(--photo-warm-b));box-shadow:0 0 1px rgba(0,0,0,.3)}
.bubble{background:var(--white);border:1px solid #d6d6d6;border-radius:16px;padding:7px 11px;font-size:16px}
.stamp{position:absolute;font-size:8px;color:var(--faint)}
.stamp--in{left:76px;top:260px}
.stamp--out{left:175px;top:330px}
.composer{position:absolute;left:24px;top:468px;width:272px;height:32px;background:var(--white);border:1px solid #d4d4d4;border-radius:16px;display:flex;align-items:center;justify-content:space-between;padding:0 12px;font-size:14px}
.composer__hint{color:var(--faint)}
.composer__send{color:var(--orange-text)}

.hero{position:absolute;left:0;top:65px;width:100%;height:456px;background:linear-gradient(180deg,#3d3530,#6d5244 35%,var(--photo-dark-a) 60%,var(--photo-dark-b))}
.hero__caption{position:absolute;left:0;top:458px;width:100%;text-align:center;font-size:19px;color:var(--white);z-index:2}
</style>
</head>
<body>
<div class="stage">

  <!-- Round result -->
  <section class="screen screen--round">
    <header class="topbar">
      <div class="status"><span class="status__carrier">●●●●○ Carrier</span><span>12:34 PM</span><span class="status__battery">100% <span class="battery"><span></span></span></span></div>
      <h1 class="title">Round 1</h1>
    </header>
    <div class="content">
      <p class="prompt">Winner of the Round<br>selects a sexual favor</p>
      <div class="player player--his">
        <svg class="player__ring" width="144" height="144" viewBox="0 0 144 144">
          <circle cx="72" cy="72" r="66" fill="none" stroke="var(--ring-his)" stroke-width="7" stroke-dasharray="302.7 500" transform="rotate(-90 72 72)"/>
          <circle cx="72" cy="72" r="59" fill="var(--white)"/>
          <circle cx="72" cy="72" r="56" fill="url(#warmA)" role="img" aria-label="Portrait photo of player Marco"/>
          <defs><radialGradient id="warmA" cx=".5" cy=".45" r=".6"><stop offset="0" stop-color="#b07a55"/><stop offset="1" stop-color="#3a2a24"/></radialGradient></defs>
        </svg>
        <span class="player__name">Marco</span>
        <span class="player__score">73%</span>
      </div>
      <div class="player player--hers">
        <svg class="player__ring" width="144" height="144" viewBox="0 0 144 144">
          <circle cx="72" cy="72" r="66" fill="none" stroke="var(--ring-hers)" stroke-width="7" stroke-dasharray="165.9 500" transform="rotate(-90 72 72)"/>
          <circle cx="72" cy="72" r="59" fill="var(--white)"/>
          <circle cx="72" cy="72" r="56" fill="url(#warmB)" role="img" aria-label="Portrait photo of player Elena"/>
          <defs><radialGradient id="warmB" cx=".5" cy=".45" r=".6"><stop offset="0" stop-color="#c09078"/><stop offset="1" stop-color="#4a3226"/></radialGradient></defs>
        </svg>
        <span class="player__name">Elena</span>
        <span class="player__score">40%</span>
      </div>
      <div class="btn-continue">Continue</div>
    </div>
    <div class="ad">
      <div class="ad__music" role="img" aria-label="Music service banner artwork"></div>
      <span class="ad__line">Human powered music discovery.</span>
      <span class="ad__chip">GET TUNEVINE FREE</span>
      <span class="ad__brand">tunevine</span>
      <span class="ad__tag">AdSpot</span>
    </div>
  </section>

  <!-- Collect favor -->
  <section class="screen screen--collect">
    <div class="dimmed">
      <header class="topbar">
        <div class="status"><span class="status__carrier">●●●●○ Carrier</span><span>12:34 PM</span><span class="status__battery">100% <span class="battery"><span></span></span></span></div>
        <h1 class="title">Round 1</h1>
      </header>
      <div class="content">
        <p class="prompt">Winner of the Round<br>selects a sexual favor</p>
        <div class="player player--his">
          <svg class="player__ring" width="144" height="144" viewBox="0 0 144 144">
            <circle cx="72" cy="72" r="66" fill="none" stroke="var(--ring-his)" stroke-width="7" stroke-dasharray="302.7 500" transform="rotate(-90 72 72)"/>
            <circle cx="72" cy="72" r="59" fill="var(--white)"/>
            <circle cx="72" cy="72" r="56" fill="#7a5440" role="img" aria-label="Portrait photo of player Marco"/>
          </svg>
          <span class="player__name">Marco</span>
          <span class="player__score">73%</span>
        </div>
        <div class="player player--hers">
          <svg class="player__ring" width="144" height="144" viewBox="0 0 144 144">
            <circle cx="72" cy="72" r="66" fill="none" stroke="var(--ring-hers)" stroke-width="7" stroke-dasharray="165.9 500" transform="rotate(-90 72 72)"/>
            <circle cx="72" cy="72" r="59" fill="var(--white)"/>
            <circle cx="72" cy="72" r="56" fill="#8a6050" role="img" aria-label="Portrait photo of player Elena"/>
          </svg>
          <span class="player__name">Elena</span>
          <span class="player__score">40%</span>
        </div>
        <div class="btn-continue">Continue</div>
      </div>
    </div>
    <div class="scrim"></div>
    <div class="sheet">
      <div class="sheet__title">Time to collect!</div>
      <ul class="sheet__list">
        <li class="sheet__item">Oral tonight</li>
        <li class="sheet__item">Be naked when I get home tomorrow</li>
        <li class="sheet__item">Naked back massage with oil</li>
        <li class="sheet__item">Naked foot massage</li>
        <li class="sheet__item">Jungle Explorer outfit</li>
      </ul>
      <div class="sheet__btn">Continue</div>
    </div>
    <div class="ad">
      <div class="ad__music" role="img" aria-label="Music service banner artwork"></div>
      <span class="ad__line">Human powered music discovery.</span>
      <span class="ad__chip">GET TUNEVINE FREE</span>
      <span class="ad__brand">tunevine</span>
      <span class="ad__tag">AdSpot</span>
    </div>
  </section>

  <!-- Waiting / chat -->
  <section class="screen screen--chat">
    <header class="topbar">
      <div class="status"><span class="status__carrier">●●●●○ Carrier</span><span>12:34 PM</span><span class="status__battery">100% <span class="battery"><span></span></span></span></div>
      <h1 class="title">Waiting for your turn</h1>
    </header>
    <div class="profile">
      <svg width="320" height="96" viewBox="0 0 320 96" style="position:absolute;left:0;top:0">
        <defs><linearGradient id="portrait" x1="0" x2="1"><stop offset="0" stop-color="#6a4a36"/><stop offset=".6" stop-color="#2b211d"/><stop offset="1" stop-color="#1c1614"/></linearGradient></defs>
        <rect width="320" height="96" fill="var(--white)"/>
        <path d="M0 0 H120 A100 100 0 0 1 164 96 H0 Z" fill="url(#portrait)" role="img" aria-label="Portrait photo of opponent Elena"/>
      </svg>
      <div class="profile__name">Elena</div>
      <div class="profile__nudge">
        <svg width="20" height="22" viewBox="0 0 20 22" aria-hidden="true"><path d="M10 1c-4 0-6 3-6 7v5l-3 4h18l-3-4V8c0-4-2-7-6-7zM7 19a3 3 0 0 0 6 0z" fill="var(--white)"/></svg>
        <span>Nudge</span>
      </div>
    </div>
    <div class="chat__label">Chat</div>
    <div class="msg msg--in"><span class="avatar" role="img" aria-label="Elena avatar photo"></span><span class="bubble">We can chat here!</span></div>
    <span class="stamp stamp--in">15:42 - 19/08/14</span>
    <div class="msg msg--out"><span class="bubble">Cool!</span><span class="avatar" role="img" aria-label="Marco avatar photo"></span></div>
    <span class="stamp stamp--out">15:46 - 19/08/14</span>
    <div class="composer"><span class="composer__hint">Message...</span><span class="composer__send">Send</span></div>
    <div class="ad">
      <div class="ad__slots" role="img" aria-label="Slot game banner artwork"></div>
      <span class="ad__store">Gadget Depot</span>
      <div class="ad__tiles"><span class="ad__tile"></span><span class="ad__tile"></span><span class="ad__tile"></span></div>
      <span class="ad__play">Play Now!</span>
      <span class="ad__tag">AdSpot</span>
    </div>
  </section>

  <!-- Turn sent -->
  <section class="screen screen--sent">
    <header class="topbar">
      <div class="status"><span class="status__carrier">●●●●○ Carrier</span><span>12:34 PM</span><span class="status__battery">100% <span class="battery"><span></span></span></span></div>
      <h1 class="title">Your turn has been sent</h1>
    </header>
    <div class="hero" role="img" aria-label="Full-screen portrait photo of opponent Elena"></div>
    <p class="hero__caption">Wait for Elena to answer...</p>
    <div class="ad">
      <div class="ad__slots" role="img" aria-label="Slot game banner artwork"></div>
      <span class="ad__store">Gadget Depot</span>
      <div class="ad__tiles"><span class="ad__tile"></span><span class="ad__tile"></span><span class="ad__tile"></span></div>
      <span class="ad__play">Play Now!</span>
      <span class="ad__tag">AdSpot</span>
    </div>
  </section>

</div>
</body>
</html>
```